Bramwell Co. Wordpress Design Project

Need a redesign of this site: http://www.thebramwellco.example/. Client wants to highlight before and after images of refinished furniture in some way that really showcases their work. Client deals with refurbishing low, middle and high end patio furniture and wants to appeal across the board. However, their bread and butter is in high end furniture refinishing. The home page should highlight everything found on their current home page including same navigation. Please show a dropdown under Residential. Use a combination of blue, white, yellow and maybe orange colors.
Updates

Reason: Client is slow to give any feedback.

Industry/Entity Type

Residential

Requirements
Must have
• Include a mini contact form on the home page. Phone number prominently displayed. Dropdown under Residential.
Nice to have
• You may feel free to use different colors in the logo in order to make it work with the design better.

```html
<!DOCTYPE html>
<html lang="en">
<head>
<meta charset="utf-8">
<title>The Bramwell Company – Patio Furniture Repair</title>
<link href="https://fonts.googleapis.com/css2?family=PT+Sans:wght@400;700&family=Arimo:wght@400;700&display=swap" rel="stylesheet">
<style>
:root{
  --orange:#f39021;
  --yellow:#f6c75a;
  --gold:#f2a81d;
  --grey-bar:#b7b7b7;
  --panel:#e3e3e3;
  --form:#c4c4c4;
  --form-head:#a9a9a9;
  --text:#444;
  --brand:#5a5a5a;
  --white:#fff;
}
*{box-sizing:border-box;margin:0;padding:0}
html,body{width:726px;height:1200px;overflow:hidden}
body{position:relative;background:var(--white);font-family:"Arimo",Arial,sans-serif;color:var(--text)}
.abs{position:absolute}
.top-line{left:0;top:0;width:726px;height:5px;background:var(--grey-bar)}
.backdrop{left:0;top:138px;width:726px;height:340px;background:linear-gradient(#ececec,#f6f6f6)}
.brand-name{left:20px;top:38px;width:160px;font-family:"PT Sans",sans-serif;font-weight:700;font-size:20px;line-height:22px;color:var(--brand)}
.phone{left:404px;top:9px;display:flex;align-items:center;gap:6px;font-family:"PT Sans",sans-serif;font-size:17px;color:#9a9a9a}
.search{left:564px;top:11px;width:130px;height:19px;border:1px solid #bbb;border-radius:10px;background:#fff}
.search svg{position:absolute;left:3px;top:2px}
.nav{left:0;top:53px;font-family:"PT Sans",sans-serif;font-size:11px;font-weight:700;color:#666;z-index:3}
.nav a{position:absolute;top:0;height:19px;line-height:19px;text-decoration:none;color:#666;white-space:nowrap}
.nav .on{background:var(--gold);color:#fff;border-radius:3px;padding:0 9px}
.nav .res{background:var(--gold);color:#222;border-radius:3px 3px 0 0;width:83px;text-align:center}
.dropdown{left:379px;top:72px;width:83px;border:2px solid var(--gold);border-top:0;background:#f2f2f2;border-radius:0 0 3px 3px;z-index:3}
.dropdown li{list-style:none;height:21px;line-height:21px;padding-left:4px;font-family:"PT Sans",sans-serif;font-size:8.5px;font-weight:700;color:#555;border-bottom:1px solid #d4d4d4;white-space:nowrap}
.dropdown li:last-child{border-bottom:0}
.slider{left:18px;top:117px;width:689px;height:347px;background:#d0d0d0;z-index:1}
.slide-text{left:28px;top:0;width:258px;height:347px;background:rgba(236,236,236,.85)}
.slide-photo{left:286px;top:0;width:403px;height:347px;background:linear-gradient(160deg,#e4e1de,#cfcccc 60%,#c07a45)}
.slide-title{left:50px;top:42px;font-family:"PT Sans",sans-serif;font-weight:700;font-size:16px;line-height:27px;color:#7a7a7a}
.slide-body{left:50px;top:168px;width:210px;font-size:8.5px;line-height:12.8px;color:#444}
.slide-body p+p{margin-top:12px}
.arrow{top:275px;width:22px;height:29px;background:var(--orange);border-radius:3px;color:#7a3a00;font-size:12px;text-align:center;line-height:29px;z-index:2}
.welcome{left:20px;top:484px;width:470px;height:247px;background:var(--panel)}
.welcome h1,.welcome h2{position:absolute;left:8px;font-family:"PT Sans",sans-serif;font-weight:700;font-size:13.5px;color:#8a8a8a}
.welcome h1{top:10px}.welcome h2{top:32px}
.welcome .copy{position:absolute;left:8px;top:70px;width:330px;font-size:8.5px;line-height:12.8px;color:#444}
.welcome .copy p+p{margin-top:12px}
.stamp{left:350px;top:482px;width:134px;height:72px;background:var(--orange);transform:rotate(8deg);border:2px solid #fff;box-shadow:0 1px 3px rgba(0,0,0,.3);text-align:center;font-family:"PT Sans",sans-serif;color:#fff;z-index:2}
.stamp .small{font-size:12px;margin-top:12px;color:#8a3c00}
.stamp .big{font-size:16px;font-weight:700}
.chair2{left:358px;top:590px;width:144px;height:156px;border-radius:14px;background:linear-gradient(135deg,#3a3430,#a45b2a)}
.btn{position:absolute;height:19px;line-height:19px;padding:0 10px;border-radius:3px;background:linear-gradient(#ffcc33,#f0a20c);border:1px solid #d88e06;color:#fff;font-family:"PT Sans",sans-serif;font-size:9px;font-weight:700;text-shadow:0 1px 0 #b46a00}
.ask{left:513px;top:484px;width:195px;height:249px;background:var(--form)}
.ask h3{height:29px;line-height:29px;padding-left:8px;background:var(--form-head);font-family:"PT Sans",sans-serif;font-size:13.5px;color:#fff}
.ask label{position:absolute;left:9px;font-size:8.5px;color:#fff}
.ask .field{position:absolute;left:45px;width:143px;height:21px;background:#fff;border:1px solid #aaa}
.ask textarea{position:absolute;left:9px;top:118px;width:179px;height:98px;border:1px solid #aaa;resize:none}
.box{top:747px;height:145px;padding:14px 14px}
.box h3{font-family:"PT Sans",sans-serif;font-size:13px;color:#222;margin-bottom:12px}
.do{left:20px;width:338px;background:linear-gradient(#f89a4c,#ea6a19)}
.do p{font-size:9.5px;line-height:13.2px;color:#5a2400;text-align:justify}
.pick{left:371px;width:337px;background:var(--yellow)}
.pick p{font-size:8.5px;line-height:13.5px;color:#4d3600}
.gallery{left:18px;top:906px;width:690px;height:222px;background:#f2f2f2}
.cell{position:absolute;top:0;height:222px;border-right:1px solid #ddd}
.after{position:absolute;top:27px;width:113px;height:138px;background:linear-gradient(#3a66c6,#1f47a0)}
.before{position:absolute;top:136px;width:74px;height:74px;border-radius:50%;background:radial-gradient(#3058b0,#17337a);border:2px solid #fff}
.sold{left:297px;top:904px;width:54px;height:30px;background:#c8242a;color:#fff;font-family:"PT Sans",sans-serif;font-weight:700;font-size:13px;text-align:center;line-height:28px;clip-path:polygon(8% 0,92% 0,100% 100%,0 100%)}
.g-arrow{top:1010px;width:16px;height:14px;background:#ddd;border:1px solid #bbb;border-radius:2px;font-size:9px;color:#777;text-align:center;line-height:12px}
.footer{left:18px;top:1139px;width:690px;height:52px;background:#f2f2f2;font-size:8.5px;color:#999}
.footer a{position:absolute;top:22px;color:#999;text-decoration:none}
.social{position:absolute;top:16px;width:20px;height:20px;border-radius:3px}
</style>
</head>
<body>
<div class="abs top-line"></div>
<div class="abs backdrop"></div>

<div class="abs brand-name">The Bramwell Company</div>

<div class="abs phone">
  <svg width="22" height="22" viewBox="0 0 22 22"><rect width="22" height="22" rx="4" fill="#9a9a9a"/><path d="M7 5c1 0 2 3 1.5 4s-.5 1 1 3 2.5 2.5 3 2 3 .5 3 1.5-1 2-2.5 1.5S7 14 6 9C5.6 7 6 5 7 5z" fill="#fff"/></svg>
  1-800-555-0147
</div>
<div class="abs search"><svg width="13" height="13" viewBox="0 0 13 13"><circle cx="5.5" cy="5.5" r="3.5" fill="none" stroke="#999" stroke-width="1.3"/><path d="M8 8l3 3" stroke="#999" stroke-width="1.5"/></svg></div>

<nav class="abs nav">
  <a class="on" style="left:250px">HOME</a>
  <a style="left:314px">ABOUT US</a>
  <a class="res" style="left:379px">RESIDENTIAL</a>
  <a style="left:477px">COMMERCIAL</a>
  <a style="left:566px">FABRICS</a>
  <a style="left:633px">CONTACT US</a>
</nav>
<ul class="abs dropdown">
  <li>Verra Marina</li><li>Ashford Coral</li><li>Ashford Vista</li><li>Marlowe Solana</li><li>Ashford Cove</li>
</ul>

<section class="abs slider">
  <div class="abs slide-photo" role="img" aria-label="Refinished white armchair with orange velvet upholstery"></div>
  <div class="abs slide-text"></div>
  <h2 class="abs slide-title">Authorized Repair/Warranty<br>Representatives for<br>Ashford Lane, Kessler,<br>Marlowe and Halvern</h2>
  <div class="abs slide-body">
    <p>The Bramwell Company has been refinishing patio furniture in the Mid-Atlantic Region since 1985. We have helped thousands of homeowners save considerably by restoring rather than replacing.</p>
    <p>We specialize in refinishing the types of high-end pool and patio furniture which was originally built to last for generations. It is difficult, if not impossible, to purchase comparable quality anywhere ...... at any price.</p>
  </div>
</section>
<div class="abs arrow" style="left:16px">(</div>
<div class="abs arrow" style="left:688px">)</div>

<section class="abs welcome">
  <h1>Welcome To The Bramwell Company!</h1>
  <h2>Patio Furniture Repair</h2>
  <div class="copy">
    <p>The Bramwell Company has been refinishing patio furniture in the Mid-Atlantic Region since 1985. We have helped thousands of homeowners save considerably by restoring rather than replacing.</p>
    <p>We specialize in refinishing the types of high-end pool and patio furniture which was originally built to last for generations. It is difficult, if not impossible, to purchase comparable quality anywhere ...... at any price.</p>
    <p>Please visit our other pages above to learn more detail of our outdoor furniture repair services or call now to receive a free estimate.</p>
  </div>
  <span class="btn" style="left:271px;top:210px">Read More</span>
</section>
<div class="abs stamp"><div class="small">DON'T REPLACE....</div><div class="big">RECYCLE !</div></div>
<div class="abs chair2" role="img" aria-label="Modern bentwood lounge chair with dark leather seat"></div>

<form class="abs ask">
  <h3>Ask a question</h3>
  <label style="top:53px">Name :</label><span class="field" style="top:45px"></span>
  <label style="top:83px">Email :</label><span class="field" style="top:75px"></span>
  <label style="top:105px">Message :</label>
  <textarea aria-label="Message"></textarea>
  <span class="btn" style="left:120px;top:223px;width:66px;text-align:center;padding:0">Submit</span>
</form>

<section class="abs box do">
  <h3>what we do</h3>
  <p>Wrought Iron Refinishing Custom Patio Furniture Sling Replacement Pool Furniture Restrapping Ashford Lane Chair Relacing Powdercoating Patio Table Repair Cast Aluminum Repainting Advice on Care and Cleaning Free Estimates by Telephone Pick Up &amp; Delivery in CT, NY, NJ, PA, DE, MD, DC, VA</p>
  <span class="btn" style="left:260px;top:110px">Read More</span>
</section>
<section class="abs box pick">
  <h3>The pick up and delivery service</h3>
  <p>When someone chooses The Bramwell Company, they are assured a professional service and product. Every piece of furniture that leaves our warehouse is 100% guaranteed. As part of the refurbishing process, you will be given instructions on how to care for your newly restored furniture to keep it looking brand new. Knowing what to use for cleaning is important. Knowing what not to use...even more so.</p>
  <span class="btn" style="left:258px;top:119px">Read More</span>
</section>

<section class="abs gallery">
  <div class="cell" style="left:0;width:213px">
    <div class="after" style="left:31px" role="img" aria-label="Refinished woven patio chair, after"></div>
    <div class="before" style="left:114px" role="img" aria-label="Same chair before refinishing"></div>
  </div>
  <div class="cell" style="left:213px;width:252px">
    <div class="after" style="left:62px" role="img" aria-label="Restrapped sling chair, after"></div>
    <div class="before" style="left:145px" role="img" aria-label="Same sling chair before restrapping"></div>
  </div>
  <div class="cell" style="left:465px;width:225px;border:0">
    <div class="after" style="left:41px" role="img" aria-label="Refinished woven patio chair, after"></div>
    <div class="before" style="left:124px" role="img" aria-label="Same chair before refinishing"></div>
  </div>
</section>
<div class="abs sold">sold</div>
<div class="abs g-arrow" style="left:24px">‹</div>
<div class="abs g-arrow" style="left:687px">›</div>

<footer class="abs footer">
  <a style="left:10px">Home</a><a style="left:55px">About us</a><a style="left:113px">Residential</a><a style="left:179px">Commercial</a><a style="left:250px">Fabrics</a><a style="left:301px">Contact us</a>
  <span class="social" style="left:588px;background:#3b5fa8"></span>
  <span class="social" style="left:617px;background:#4aa8d8"></span>
  <span class="social" style="left:646px;background:#f08a1c"></span>
  <a style="left:672px">x12</a>
</footer>
</body>
</html>
```